Strong, modern, clean Business Card design

Looking for a stunning, but CLEAN business card design. While we are a faith-based organization, we do NOT want this to look religious.

Industry/Entity Type

Non-Profit

Contact Information for Business Card

Dale Munroe | Lead Pastor
dale@BrightHarvestHope.org
970-555-0148
PO Box 7316
Pine Hollow, MT 80571

Font styles to use
Serif
Sans Serif

Requirements
Should not have
• Religious imagery or symbolism

```html
<!DOCTYPE html>
<html lang="en">
<head>
<meta charset="UTF-8">
<title>Dale Munroe – Business Card</title>
<link href="https://fonts.googleapis.com/css2?family=Montserrat:wght@300;600;700&family=Comfortaa:wght@400&family=Playfair+Display:wght@400;600&display=swap" rel="stylesheet">
<style>
  :root {
    --page: #fdfdfd;
    --card: #e6e7e9;
    --brand-blue: #4d7a93;
    --ink: #2f2f31;
    --rule: #5a5a5c;
  }
  html, body {
    margin: 0;
    width: 1200px;
    height: 1200px;
    overflow: hidden;
    background: var(--page);
  }
  .business-card {
    position: absolute;
    left: 169px;
    top: 407px;
    width: 839px;
    height: 480px;
    background: var(--card);
    overflow: hidden;
  }
  .card-footer-band {
    position: absolute;
    left: 0;
    bottom: 0;
    width: 100%;
    height: 11px;
    background: var(--brand-blue);
  }
  .brand-mark {
    position: absolute;
    left: 141px;
    top: 159px;
    width: 104px;
    height: 105px;
    border-radius: 15px;
    background: var(--brand-blue);
  }
  .brand-name {
    position: absolute;
    left: 43px;
    top: 284px;
    width: 300px;
    margin: 0;
    text-align: center;
    font-family: "Playfair Display", serif;
    font-weight: 600;
    font-size: 26px;
    line-height: 32px;
    letter-spacing: 1px;
    color: var(--brand-blue);
    text-transform: uppercase;
  }
  .brand-name .brand-sub {
    display: block;
    font-weight: 400;
    font-size: 18px;
    line-height: 26px;
    letter-spacing: 17px;
    padding-left: 17px;
  }
  .divider {
    position: absolute;
    left: 366px;
    top: 101px;
    width: 1.5px;
    height: 282px;
    background: var(--rule);
  }
  .person-name {
    position: absolute;
    left: 399px;
    top: 106px;
    margin: 0;
    font-family: "Montserrat", sans-serif;
    font-size: 46px;
    line-height: 56px;
    letter-spacing: -1.5px;
    color: var(--brand-blue);
    white-space: nowrap;
  }
  .person-name .first { font-weight: 700; }
  .person-name .last { font-weight: 300; }
  .person-title {
    position: absolute;
    left: 404px;
    top: 157px;
    margin: 0;
    font-family: "Montserrat", sans-serif;
    font-weight: 300;
    font-size: 15px;
    letter-spacing: 12.5px;
    color: var(--ink);
    text-transform: uppercase;
  }
  .contact-list {
    position: absolute;
    left: 400px;
    top: 231px;
    margin: 0;
    padding: 0;
    list-style: none;
  }
  .contact-item {
    display: flex;
    align-items: center;
    height: 52px;
  }
  .contact-icon {
    width: 30px;
    height: 42px;
    flex: none;
  }
  .contact-text {
    margin-left: 27px;
    font-family: "Comfortaa", sans-serif;
    font-size: 19px;
    color: var(--ink);
    white-space: nowrap;
  }
</style>
</head>
<body>
  <section class="business-card">
    <div class="brand-mark"></div>
    <p class="brand-name">Bright Harvest<span class="brand-sub">Church</span></p>

    <div class="divider"></div>

    <h1 class="person-name"><span class="first">DALE</span> <span class="last">MUNROE</span></h1>
    <p class="person-title">Lead Pastor</p>

    <ul class="contact-list">
      <li class="contact-item">
        <svg class="contact-icon" viewBox="0 0 30 42" aria-hidden="true">
          <rect x="2" y="1" width="25" height="40" rx="3" fill="none" stroke="var(--ink)" stroke-width="1.3"/>
          <line x1="2" y1="6" x2="27" y2="6" stroke="var(--ink)" stroke-width="1.1"/>
          <line x1="2" y1="35" x2="27" y2="35" stroke="var(--ink)" stroke-width="1.1"/>
          <line x1="11" y1="38" x2="18" y2="38" stroke="var(--ink)" stroke-width="1.5"/>
        </svg>
        <span class="contact-text">406-555-0148</span>
      </li>
      <li class="contact-item">
        <svg class="contact-icon" viewBox="0 0 30 42" aria-hidden="true">
          <circle cx="15" cy="21" r="6" fill="none" stroke="var(--ink)" stroke-width="1.3"/>
          <path d="M21 15 V24 Q21 28 25 27 Q29 25 29 20 A14 14 0 1 0 22 33" fill="none" stroke="var(--ink)" stroke-width="1.3"/>
        </svg>
        <span class="contact-text">dale@BrightHarvestHope.org</span>
      </li>
      <li class="contact-item">
        <svg class="contact-icon" viewBox="0 0 30 42" aria-hidden="true">
          <path d="M15 37 C9 30 2 24 2 16 A13 13 0 0 1 28 16 C28 24 21 30 15 37 Z" fill="none" stroke="var(--ink)" stroke-width="1.3"/>
          <circle cx="15" cy="16" r="5" fill="none" stroke="var(--ink)" stroke-width="1.3"/>
        </svg>
        <span class="contact-text">PO Box 7316 Pine Hollow, MT 80571</span>
      </li>
    </ul>

    <div class="card-footer-band"></div>
  </section>
</body>
</html>
```